Need Visually Stunning Banner Ad

Need 2 visually stunning banners for my website. Each banner of a specific size requires a different color scheme (800x600 grey, white and golden yellow) AND (468x60 pink and blue accents). I'm not a fan of my current banner but it shows how you can change the logo to fit a 468x60 banner.

Each banner should be static, have the logo in some form or fashion, the url www.velmoridanqq.com and if you can fit the line "Elite Escort Booking Service". Please make it stylish with the ability to stand out from the rest.

Target Market(s)

Chic stylish female entertainers

Font styles to use
Sans Serif

Requirements
Must have
• Style
Should not have
• animation or flash

```html
<!DOCTYPE html>
<html lang="en">
<head>
<meta charset="utf-8">
<title>Velmoridanqq – Banner Set</title>
<link href="https://fonts.googleapis.com/css2?family=Montserrat:wght@500;800&family=Great+Vibes&display=swap" rel="stylesheet">
<style>
  :root {
    --stage: #c9cfcf;
    --charcoal: #2f2f31;
    --charcoal-soft: #454547;
    --shirt-light: #d9d6d2;
    --shirt-mid: #9c9892;
    --skin-warm: #c98f6e;
    --hair-brown: #6a3f2c;
    --gold: #f5ab00;
    --gold-veil: rgba(245, 171, 0, 0.55);
    --white: #ffffff;
    --pink: #ff5a7e;
    --navy: #1c3a78;
    --violet: #6b4a9a;
  }
  * { margin: 0; padding: 0; box-sizing: border-box; }
  html, body {
    width: 1200px;
    height: 1200px;
    overflow: hidden;
    background: var(--stage);
    font-family: "Montserrat", sans-serif;
  }
  .canvas { position: relative; width: 1200px; height: 1200px; }

  /* ---------- 800x600 banner ---------- */
  .banner-large {
    position: absolute;
    left: 121px; top: 121px;
    width: 960px; height: 720px;
    overflow: hidden;
    box-shadow: 0 4px 10px rgba(0,0,0,0.25);
    background: var(--charcoal);
  }
  .banner-large .photo {
    position: absolute; inset: 0;
    background:
      radial-gradient(ellipse 11% 15% at 28% 24%, var(--skin-warm) 0%, rgba(201,143,110,0) 100%),
      radial-gradient(ellipse 20% 26% at 26% 20%, var(--hair-brown) 0%, rgba(106,63,44,0) 100%),
      radial-gradient(ellipse 30% 38% at 30% 66%, var(--shirt-light) 0%, rgba(217,214,210,0.5) 45%, rgba(156,152,146,0) 100%),
      radial-gradient(ellipse 14% 30% at 8% 32%, var(--shirt-mid) 0%, rgba(156,152,146,0) 100%),
      radial-gradient(ellipse 10% 24% at 44% 38%, var(--shirt-mid) 0%, rgba(156,152,146,0) 100%),
      linear-gradient(90deg, var(--charcoal-soft) 0%, var(--charcoal) 62%, var(--charcoal) 100%);
  }
  .banner-large .accents { position: absolute; inset: 0; }
  .banner-large .copy {
    position: absolute;
    left: 520px; top: 112px;
    width: 296px;
    text-align: center;
    color: var(--white);
  }
  .script-elite {
    font-family: "Great Vibes", cursive;
    font-weight: 400;
    color: var(--gold);
    line-height: 1;
  }
  .banner-large .script-elite {
    display: block;
    font-size: 92px;
    margin-bottom: -26px;
  }
  .banner-large .headline {
    font-weight: 800;
    font-size: 57px;
    line-height: 54px;
    text-transform: uppercase;
  }
  .brand-mark {
    display: flex;
    flex-direction: column;
    align-items: center;
    justify-content: center;
    color: var(--white);
    font-weight: 800;
  }
  .brand-mark .ring {
    border-radius: 50%;
    border: 4px solid var(--white);
    flex: none;
  }
  .banner-large .brand-mark {
    position: absolute;
    left: 518px; top: 414px;
    width: 300px; height: 174px;
    gap: 18px;
    font-size: 30px;
    letter-spacing: 3px;
  }
  .banner-large .brand-mark .ring { width: 96px; height: 96px; }
  .banner-large .site-url {
    position: absolute;
    left: 518px; top: 628px;
    width: 300px;
    text-align: center;
    color: var(--white);
    font-weight: 500;
    font-size: 22px;
  }

  /* ---------- 468x60 banner ---------- */
  .banner-leaderboard {
    position: absolute;
    left: 319px; top: 976px;
    width: 562px; height: 72px;
    overflow: hidden;
    background: var(--pink);
    box-shadow: 0 3px 8px rgba(0,0,0,0.22);
  }
  .banner-leaderboard .photo {
    position: absolute; left: 0; top: 0;
    width: 119px; height: 72px;
    background:
      radial-gradient(ellipse 22% 34% at 55% 38%, var(--skin-warm) 0%, rgba(201,143,110,0) 100%),
      radial-gradient(ellipse 36% 70% at 55% 40%, var(--hair-brown) 0%, rgba(106,63,44,0) 100%),
      linear-gradient(180deg, rgba(255,90,126,0) 60%, #e04a6a 100%),
      linear-gradient(90deg, var(--pink) 0%, #f07a8a 100%);
  }
  .banner-leaderboard .accents { position: absolute; inset: 0; }
  .banner-leaderboard .tagline {
    position: absolute;
    left: 124px; top: 0;
    height: 72px;
    display: flex;
    align-items: center;
    gap: 8px;
    color: var(--white);
  }
  .banner-leaderboard .script-elite {
    color: var(--navy);
    font-size: 36px;
  }
  .banner-leaderboard .headline {
    font-weight: 800;
    font-size: 16px;
    letter-spacing: 0.3px;
    text-transform: uppercase;
  }
  .banner-leaderboard .brand-mark {
    position: absolute;
    left: 472px; top: 0;
    width: 90px; height: 72px;
    gap: 6px;
    font-size: 9.5px;
    letter-spacing: 0.3px;
  }
  .banner-leaderboard .brand-mark .ring { width: 22px; height: 22px; border-width: 2px; }
</style>
</head>
<body>
<main class="canvas">

  <section class="banner-large" aria-label="800 by 600 banner">
    <div class="photo" role="img" aria-label="Photo of a relaxed woman in a white plaid shirt, hands behind her head, in a dim café"></div>
    <svg class="accents" viewBox="0 0 960 720" width="960" height="720" aria-hidden="true">
      <polygon points="835,0 960,0 960,353" fill="var(--gold-veil)"/>
      <polygon points="835,0 960,0 960,134" fill="var(--gold)"/>
      <polygon points="0,329 0,720 227,720" fill="var(--gold-veil)"/>
      <polygon points="0,581 0,720 227,720" fill="var(--gold)"/>
    </svg>
    <div class="copy">
      <span class="script-elite">Elite</span>
      <h1 class="headline">Escort<br>Booking<br>Service</h1>
    </div>
    <div class="brand-mark"><span class="ring"></span><span class="brand-name">VELMORIDANQQ</span></div>
    <p class="site-url">www.velmoridanqq.com</p>
  </section>

  <section class="banner-leaderboard" aria-label="468 by 60 banner">
    <div class="photo" role="img" aria-label="Portrait photo of a smiling woman with a pink scarf"></div>
    <svg class="accents" viewBox="0 0 562 72" width="562" height="72" aria-hidden="true">
      <polygon points="0,0 12,0 0,20" fill="var(--navy)"/>
      <polygon points="468,0 486,0 468,72 450,72" fill="var(--violet)"/>
      <polygon points="486,0 562,0 562,72 468,72" fill="var(--navy)"/>
    </svg>
    <div class="tagline">
      <span class="script-elite">Elite</span>
      <span class="headline">Escort Booking Service</span>
    </div>
    <div class="brand-mark"><span class="ring"></span><span class="brand-name">VELMORIDANQQ</span></div>
  </section>

</main>
</body>
</html>
```